Bellwether Recovery Brochure for a drug and alcohol addiction treatment center.

***Update #2***
For graphic highlights no intrusion into text and no fade into adjoining areas.Use modern clean white layout with grey and light orange color scheme. Use attached yoga photo and other photos. For cover try moving number and logo around, and also try with cover photo not full size. Also use larger text with bullet points in a couple spots. Also try with new attached cover photos.
***Update*** I have attached some new photos to clarify the design wanted. My client likes the size (but not design) of the brochure in the newly included photos. Note the measurements - when closed it is 6" wide x 7" tall. When fully open it is 18" long, 7" wide, with 2 folds. I apologize if my terminology below was confusing. Please confirm that your design reflects the desired layout, and please modify your design if it does not. Thanks!
Want a trifold brochure 6" wide x 7" height. Design is for a drug and alcohol addiction treatment center. We want clean, soft, contemporary with highlight colors orange and grey, with contemporary font. Maybe some soft curves on design - see this A4 design we like but not the colors:
http://quillstockmart.net/item/business-trifold-brochure-wave/7315920?s_phrase=trifold%20business%20brochure&s_rank=54
See company web site for style cues and some content you can use:
http://bellwetherrecovery.com/
You can use the attached photos and logo in the design. Try sun in hand photo on cover, or man on beach. Please do not use the words "The Bellwether Recovery Center" in verbiage or titles, for business reasons we want to use "Bellwether Recovery Center" with no "The" instead.
Please note that the logo has been updated. The new logo is attached below. Use bellwether rev2.png for logo.
Addiction treatment industry professionals; family and decision makers of addict; addict themselves.

```html
<!DOCTYPE html>
<html lang="en">
<head>
<meta charset="utf-8">
<title>Bellwether Recovery Center – Trifold Brochure</title>
<link href="https://fonts.googleapis.com/css2?family=Questrial&family=Montserrat:wght@500;600&family=Crimson+Text:ital@1&display=swap" rel="stylesheet">
<style>
  :root{
    --orange:#f07a1e;
    --orange-light:#f9a24a;
    --grey:#4a4a4a;
    --grey-text:#3c3c3c;
    --paper:#ffffff;
    --stage:#e9e9e9;
    --night:#1c1830;
  }
  *{margin:0;padding:0;box-sizing:border-box}
  html,body{width:1200px;height:1032px;overflow:hidden;background:var(--stage)}
  body{position:relative;font-family:"Questrial",sans-serif;color:var(--grey-text)}
  .spread{position:absolute;left:58px;width:1082px;height:422px;background:var(--paper);overflow:hidden;box-shadow:0 2px 8px rgba(0,0,0,.18)}
  .spread--outside{top:56px}
  .spread--inside{top:526px}
  .abs{position:absolute}
  .photo{position:absolute}
  .body-copy{position:absolute;font-size:7.1px;line-height:9.6px;text-align:justify;color:var(--grey-text)}
  .body-copy p+p{margin-top:0}
  .section-title{position:absolute;font-size:22px;color:var(--orange);line-height:1}
  .panel-title{position:absolute;font-size:17px;line-height:19px;color:var(--grey)}
  .panel-title span{display:block;color:var(--orange)}
  .pull-quote{position:absolute;font-family:"Crimson Text",serif;font-style:italic;font-size:7.6px;line-height:10px;color:var(--grey)}
  .pull-quote::before{content:"\201C";position:absolute;left:-16px;top:-6px;font-family:"Montserrat",sans-serif;font-style:normal;font-weight:600;font-size:20px;color:var(--orange)}
  .pull-quote::after{content:"\201D";position:absolute;right:-2px;bottom:-18px;font-family:"Montserrat",sans-serif;font-style:normal;font-weight:600;font-size:20px;color:var(--orange)}
  .wave{position:absolute}
  .cta-line{position:absolute;left:32px;font-size:17px;color:var(--grey)}
  .cta-call{position:absolute;left:32px;font-family:"Montserrat",sans-serif;font-weight:600;font-size:16px;color:var(--orange)}
  .cover-name{position:absolute;left:362px;top:0;width:720px;height:422px}
  .brand-mark{position:absolute;left:810px;top:212px;width:170px;text-align:center;color:#fff;font-family:"Montserrat",sans-serif;font-weight:600;line-height:1}
  .brand-mark .brand-main{display:block;font-size:26px;letter-spacing:.3px}
  .brand-mark .brand-sub{display:block;font-size:13.5px;margin-top:3px}
  .brand-dot{position:absolute;left:866px;top:148px;width:58px;height:58px;border:3px solid #fff;border-radius:50%}
  .cover-contact{position:absolute;left:392px;top:342px;color:#fff}
  .cover-contact .org{font-family:"Montserrat",sans-serif;font-weight:600;font-size:11.5px}
  .cover-contact .addr{font-size:12px;margin-top:4px}
  .cover-contact .tel{font-size:15px;margin-top:5px}
</style>
</head>
<body>

<section class="spread spread--outside" aria-label="Brochure outside">
  <h2 class="section-title" style="left:28px;top:32px">About Us</h2>
  <div class="body-copy" style="left:28px;top:56px;width:306px">
    <p>Bellwether Recovery Center offers affordable treatment for a wide variety of addictions. We address underlying psychological disorders and specialize in treatment for drug addiction and alcoholism. At Bellwether Recovery Center we feature a full spectrum of addiction treatment programs, from initial assessment and detox, to inpatient residential and intensive outpatient care, as well as transitional housing and sober living environments for extended care.</p>
    <p>At Bellwether Recovery Center we believe strongly in a holistic approach to recovery through treating the mind, body, and soul. To facilitate this holistic recovery perspective we promote a healthy diet for our clients, and physical fitness through visits to a nationally recognized gym. In addition, guided yoga and meditation, hiking trips in Southern California's beautiful natural areas, and trips to the areas world-famous beaches are available during a client's stay.</p>
  </div>
  <div class="photo" role="img" aria-label="Photo of the center's sunny courtyard with patio tables and trees" style="left:0;top:174px;width:358px;height:160px;background:linear-gradient(180deg,#fff 0%,#d9cfc2 18%,#a89a86 55%,#7f8a6a 100%)"></div>
  <svg class="wave" style="left:0;top:300px" width="358" height="60" viewBox="0 0 358 60" preserveAspectRatio="none">
    <path d="M0 20 C90 36 200 0 358 14 L358 60 L0 60Z" fill="var(--orange-light)"/>
    <path d="M0 30 C100 46 210 14 358 26 L358 60 L0 60Z" fill="var(--orange)"/>
    <path d="M0 42 C110 58 230 26 358 34 L358 60 L0 60Z" fill="#fff"/>
  </svg>
  <div class="cta-line" style="top:358px">Recover from Addiction</div>
  <div class="cta-call" style="top:380px">Call 855-555-0142 Now</div>

  <div class="cover-name" role="img" aria-label="Photo of a lighthouse silhouetted against a golden sunset over the sea" style="background:radial-gradient(circle at 40% 20%,#fff6d8 0%,#ffc247 10%,#e98a2a 28%,rgba(120,80,110,.9) 55%,rgba(40,60,120,.95) 80%),linear-gradient(180deg,#2b5fa8 0%,#4a4070 60%,var(--night) 100%)"></div>
  <div class="abs" aria-hidden="true" style="left:362px;top:270px;width:720px;height:152px;background:linear-gradient(180deg,rgba(28,24,48,0) 0%,rgba(28,24,48,.85) 50%,var(--night) 100%)"></div>
  <div class="brand-dot" aria-hidden="true"></div>
  <div class="brand-mark"><span class="brand-main">BELLWETHER</span><span class="brand-sub">RECOVERY CENTER</span></div>
  <div class="cover-contact">
    <div class="org">BELLWETHER RECOVERY CENTER</div>
    <div class="addr">1482 Linden Ave, Fairmont CA</div>
    <div class="tel">Tel.&nbsp; 855-555-0142</div>
  </div>
</section>

<section class="spread spread--inside" aria-label="Brochure inside">
  <!-- panel: alcohol rehab -->
  <h3 class="panel-title" style="left:26px;top:34px">Bellwether<span>Alcohol Rehab</span></h3>
  <blockquote class="pull-quote" style="left:183px;top:38px;width:150px">The alcohol rehab programs focus on building life skills that are necessary for successful, long-term healing.</blockquote>
  <div class="body-copy" style="left:24px;top:102px;width:308px">
    <p>Bellwether Recovery Center offers a contemporary approach to recovery from alcoholism. We recognize the necessity of treating the underlying issues from a psychological perspective, combining this with time-tested methods such as 12 step programs, and creating a synergy between these with a holistic approach to the individual.</p>
    <p>Our alcohol and drug treatment programs typically include a residential component, which is available after detox or in cases when detox is not part of the individual treatment plan. Bellwether Recovery Center features a newly renovated alcohol and drug treatment facility- the drug rehab is located in sunny Fairmont, only 1 mile from world-famous Harborland Park and about 20 miles from beautiful Seacliff Beach. Our facility offers a homelike feel with airy rooms, which helps to provide a safe and comfortable environment for healing from the devastating consequences of alcoholism.</p>
  </div>
  <div class="photo" role="img" aria-label="Photo of a hiker with a backpack standing in a golden wheat field under a bright sky" style="left:0;top:234px;width:362px;height:188px;background:linear-gradient(180deg,#fff 0%,#cfe2f3 20%,#8fb7de 50%,#d9b25a 70%,#b8862e 100%)"></div>

  <!-- panel: detox -->
  <div class="photo" role="img" aria-label="Photo of a gravel path through green grass toward a low sun" style="left:362px;top:22px;width:362px;height:154px;background:linear-gradient(180deg,#eef3f7 0%,#cfd9c4 30%,#8e9d5a 60%,#5a6e2e 100%)"></div>
  <svg class="wave" style="left:362px;top:140px" width="362" height="50" viewBox="0 0 362 50" preserveAspectRatio="none">
    <path d="M0 30 C110 0 240 18 362 4 L362 50 L0 50Z" fill="var(--orange-light)"/>
    <path d="M0 36 C120 10 250 26 362 14 L362 50 L0 50Z" fill="var(--orange)"/>
    <path d="M0 44 C130 24 260 36 362 30 L362 50 L0 50Z" fill="#fff"/>
  </svg>
  <h3 class="panel-title" style="left:386px;top:208px">Bellwether<span>Detox Center</span></h3>
  <blockquote class="pull-quote" style="left:537px;top:210px;width:160px">Although it is true that drug and alcohol detox may be the first step in seeking help, not all drug or alcohol addicted people will require detoxification.</blockquote>
  <div class="body-copy" style="left:384px;top:268px;width:308px">
    <p>Some clients may directly enter the residential treatment program, or, depending on the results of the assessment, it may be suggested that they enter our intensive outpatient or partial hospitalization programs. Family members or loved ones seeking a detox center for an alcoholic or addict should ask about our family intervention services. Sometimes through intervention we can help begin your loved ones journey into recovery.</p>
    <p>At times when a client suffers from severe decompensation, we typically refer him or her immediately to a facility for hospital detox services. In those cases that do not require such a level of care, we feature clinically managed detox at our facility. Note that our facility is licensed for residential detox. Residential detox services at Bellwether Recovery Center provide for managed medication, and the detox services are administered by an independent medical doctor. The detox doctor is board-certified and specializes in addiction medicine.</p>
  </div>

  <!-- panel: drug rehab -->
  <h3 class="panel-title" style="left:748px;top:40px">Bellwether<span>Drug Rehab</span></h3>
  <blockquote class="pull-quote" style="left:890px;top:42px;width:166px">Bellwether offers a full array of affordable drug rehab programs that can take addicts from detox to inpatient or outpatient care and back home again.</blockquote>
  <div class="body-copy" style="left:746px;top:102px;width:308px">
    <p>An extensive assessment is performed on each client that come to us for drug rehab. Medication management is provided on site with medical supervision. We are committed to providing intensive support to assist our clients in getting through this phase. If acute detox care is required, we refer our clients to inpatient hospital detox, where they are treated offsite until they are ready for treatment in our facilities.</p>
    <p>The next step in our drug treatment programs is inpatient residential treatment, which takes place in our modern alcohol rehab and drug rehab facility, located in sunny Fairmont, only 1 mile from world-famous Harborland Park and about 20 miles from beautiful Seacliff Beach. If not necessary to go through formal detox before entering the residential program, so clients may go directly from their assessment into inpatient residential care. In the residential program treatment focuses on comprehensive individual therapy and group therapy with peers. Medication management is provided on site with medical supervision. Each client has access to Guided Yoga and Meditation, and transportation to a nationally recognized athletic club five days a week. Saturday is set aside as a day dedicated to family group activities and approved visitations.</p>
  </div>
  <div class="photo" role="img" aria-label="Photo of a hiker resting on rocks above the sea at sunset" style="left:724px;top:270px;width:358px;height:152px;background:linear-gradient(180deg,#fff 0%,#f3e6cf 25%,#d9b98a 55%,#7d8a8c 80%,#4b4a3e 100%)"></div>
</section>

</body>
</html>
```